I need a website built for my organization.
We are the world's largest network of music producers.
The website should be professional, sharp, and high quality., We need a website built for The Halvern Sound Guild. We are one of the World's largest association of music producers.
The site must be professional, sharp, and high quality., I need a website built for my organization.
The site must be professional, sharp, and high quality.
Somewhere in the top half of the site there should be a form for the user to fill out. The details of the form are as follows:
Title (large and bold): Contact Us or Submit Your Music
Fields to include (* = required): First Name*, Last Name*, Age, Zip Code, Email Address*, Daytime Phone, Evening Phone, Comments
Then, there will be a "submit" button to proceed to next step of form. Just below the "submit" button, should be the following verbiage: "After submitting, you will have the opportunity to upload demos of your music (optional) and provide other pertinent information about yourself, band, or group."
Target Market(s)
Music producers and aspiring musicians
Industry/Entity Type
Group
Colors
Designer to choose colors to be used in the design.
Look and feel

```html
<!DOCTYPE html>
<html lang="en">
<head>
<meta charset="utf-8">
<title>The Halvern Sound Guild</title>
<link rel="stylesheet" href="https://fonts.googleapis.com/css2?family=PT+Serif:wght@400;700&family=Roboto:wght@400;500&display=swap">
<style>
:root{
  --black:#050505;
  --ink:#111;
  --gold:#e0b84f;
  --gold-light:#d9c27d;
  --gold-dark:#8a6a1e;
  --white:#fff;
  --field:#f7f7f7;
  --muted:#6f6f6f;
  --footer-link:#9a9a9a;
  --rule:#bdbdbd;
}
*{box-sizing:border-box;margin:0;padding:0}
html,body{width:1175px;height:1200px;overflow:hidden;background:var(--white)}
body{position:relative;font-family:"Roboto",sans-serif;color:var(--ink)}
.hero{position:absolute;left:0;top:0;width:1175px;height:766px;background:var(--black)}
.hero-photo{position:absolute;left:0;top:0;width:1030px;height:701px;
  background:radial-gradient(ellipse 420px 380px at 300px 300px,#7c97a8 0%,#3e5566 45%,#152029 75%,rgba(5,5,5,0) 100%),
  linear-gradient(90deg,#0c1218 0%,#22313c 30%,#1a252e 55%,rgba(5,5,5,0.9) 85%,var(--black) 100%)}
.band{position:absolute;left:0;top:701px;width:1175px;height:65px;background:#0d0d0d}
.brand{position:absolute;left:186px;top:58px;display:flex;align-items:center;gap:10px;
  font-family:"PT Serif",serif;font-size:30px;color:var(--gold);letter-spacing:3px;text-transform:uppercase}
.brand-dot{width:12px;height:12px;border-radius:50%;background:var(--gold)}
.account{position:absolute;left:911px;top:33px;font-family:"PT Serif",serif;font-weight:700;font-size:12px;letter-spacing:1px;color:var(--white)}
.account span{color:var(--gold)}
.nav{position:absolute;top:66px;left:674px;font-family:"PT Serif",serif;font-size:15.5px;color:var(--white)}
.nav a{position:absolute;white-space:nowrap;color:var(--white);text-decoration:none}
.nav .sep{position:absolute;color:var(--white)}
.headline{position:absolute;left:592px;top:147px;width:480px;font-family:"PT Serif",serif;font-size:39px;line-height:47px;color:var(--white);font-weight:400}
.form-title{position:absolute;left:595px;top:290px;font-family:"PT Serif",serif;font-size:22px;color:var(--white);text-transform:uppercase;white-space:nowrap}
.form-title .accent{color:var(--gold)}
.form-title .big{font-size:33px}
.field{position:absolute;height:39px;border:0;background:var(--field);padding:0 13px;font-family:"Roboto",sans-serif;font-size:12px;color:#444}
.field::placeholder{color:#555}
textarea.field{height:98px;padding-top:13px;resize:none}
.submit{position:absolute;left:594px;top:611px;width:215px;height:43px;border:0;
  background:linear-gradient(180deg,#e9d9a2 0%,#cdb160 50%,#b8993f 100%);
  font-family:"PT Serif",serif;font-weight:700;font-size:18px;color:var(--gold-dark)}
.form-note{position:absolute;left:595px;top:670px;width:460px;font-size:11.5px;line-height:17.5px;color:var(--muted)}
.card{position:absolute;top:795px;width:295px}
.card-img{width:295px;height:165px}
.card h2{margin-top:12px;font-family:"PT Serif",serif;font-weight:400;font-size:18.5px;letter-spacing:1.5px;text-transform:uppercase;color:var(--ink)}
.card p{margin-top:6px;font-size:12.3px;line-height:18px;color:#222}
.card p a{color:var(--ink);text-decoration:underline}
.divider{position:absolute;left:127px;top:1088px;width:920px;height:1px;background:var(--rule)}
.footer{position:absolute;left:0;top:1090px;width:1175px;height:110px;background:var(--black)}
.footer-brand{position:absolute;left:200px;top:40px;display:flex;align-items:center;gap:8px;font-family:"PT Serif",serif;font-size:24px;letter-spacing:2px;color:var(--gold);text-transform:uppercase}
.footer-brand .brand-dot{width:10px;height:10px}
.footer-col{position:absolute;top:41px;list-style:none;font-size:12.3px;font-weight:500;line-height:17.6px}
.footer-col a{color:var(--footer-link);text-decoration:none}
.social{position:absolute;top:52px;width:32px;height:32px;border-radius:50%;background:#5a5a5a}
</style>
</head>
<body>
<header class="hero">
  <div class="hero-photo" role="img" aria-label="Concert photo: silhouette of a guitarist on stage with raised arm, blue stage light and crowd"></div>
  <div class="band"></div>
  <div class="brand"><span class="brand-dot"></span>Halvern</div>
  <div class="account">LOGIN | <span>REGISTER</span></div>
  <nav class="nav">
    <a style="left:0">Home</a><span class="sep" style="left:68px">|</span>
    <a style="left:99px">Members</a><span class="sep" style="left:186px">|</span>
    <a style="left:215px">About</a><span class="sep" style="left:282px">|</span>
    <a style="left:311px">Contact</a>
  </nav>
  <h1 class="headline">We turn aspiring musicians into SuperStars!</h1>
  <form>
    <h2 class="form-title"><span class="accent"><span class="big">C</span>ontact</span> us or <span class="accent">submit</span> music demo</h2>
    <input class="field" style="left:594px;top:336px;width:215px" placeholder="First Name">
    <input class="field" style="left:831px;top:336px;width:215px" placeholder="Last Name">
    <input class="field" style="left:594px;top:388px;width:101px" placeholder="Age">
    <input class="field" style="left:713px;top:388px;width:96px" placeholder="Zip Code">
    <input class="field" style="left:831px;top:388px;width:215px" placeholder="Email Address">
    <input class="field" style="left:594px;top:441px;width:215px" placeholder="Daytime Phone">
    <input class="field" style="left:831px;top:441px;width:215px" placeholder="Evening Time Phone">
    <textarea class="field" style="left:594px;top:494px;width:452px" placeholder="Comments"></textarea>
    <button class="submit" type="button">Submit Form</button>
    <p class="form-note">After submitting, you will have the opportunity to upload demos of your music (optional) and provide other pertinent information about yourself, band, or group.</p>
  </form>
</header>

<section class="card" style="left:126px">
  <div class="card-img" role="img" aria-label="High-contrast photo of a guitarist silhouette holding a guitar" style="background:linear-gradient(90deg,#0a0a0a 0%,#1a1a1a 60%,#e8e8e8 100%)"></div>
  <h2>What we do</h2>
  <p>Lorem ipsum dolor sit amet, consectetur adipisicing elit, sed do eiusmod tempor incididunt ut labore et dolore magna aliqua. <a>Read More</a></p>
</section>
<section class="card" style="left:440px">
  <div class="card-img" role="img" aria-label="Collage of concert photos of rock performers" style="background:linear-gradient(120deg,#5a1e1a 0%,#2b2a8c 45%,#1b1b1b 70%,#2d6a9a 100%)"></div>
  <h2>Latest news</h2>
  <p>Lorem ipsum dolor sit amet, consectetur adipisicing elit, sed do eiusmod tempor incididunt ut labore et dolore magna aliqua. <a>Read More</a></p>
</section>
<section class="card" style="left:752px">
  <div class="card-img" role="img" aria-label="Black and white portrait of the featured artist" style="background:linear-gradient(90deg,#2a2a2a 0%,#8a8a8a 50%,#d5d5d5 100%)"></div>
  <h2>Artist of the month</h2>
  <p>Lorem ipsum dolor sit amet, consectetur adipisicing elit, sed do eiusmod tempor incididunt ut labore et dolore magna aliqua. <a>Read More</a></p>
</section>

<div class="divider"></div>

<footer class="footer">
  <div class="footer-brand"><span class="brand-dot"></span>Halvern</div>
  <ul class="footer-col" style="left:440px"><li><a>Home</a></li><li><a>About</a></li><li><a>Contact</a></li></ul>
  <ul class="footer-col" style="left:595px"><li><a>Members</a></li><li><a>Agencies</a></li><li><a>News</a></li></ul>
  <ul class="footer-col" style="left:754px"><li><a>Privacy Policy</a></li><li><a>Sitemap</a></li></ul>
  <span class="social" style="left:911px"></span>
  <span class="social" style="left:958px"></span>
  <span class="social" style="left:1005px"></span>
</footer>
</body>
</html>
```